Business Card Redesign

We would like to redesign our existing business cards.
The new design shall look:
ELEGANT, LUXURY, PROFESSIONAL
Reference:
YOU CAN VISIT WWW.LUMEN-BRIDGE-PARTNERS.EXAMPLE FOR BETTER UNDERSTANDING OF COMPANY STRATEGY AND POSITION
Additional:
CHOSEN CANDIDATE SHALL PROVIDE THE INSTRUCTION OF PRINTING IF ANY THERMAL COVERAGE OR ANY ADDITION IS OFFERED
Industry/Entity Type
Business

```html
<!DOCTYPE html>
<html lang="en">
<head>
<meta charset="utf-8">
<title>Lumen Bridge Partners Limited – Business Card</title>
<link rel="stylesheet" href="https://fonts.googleapis.com/css2?family=Open+Sans:wght@400;600&family=Crimson+Text:wght@400&display=swap">
<style>
  :root {
    --backdrop: #2f3033;
    --gold: #e8ac35;
    --navy: #0c5a96;
    --paper: #e5e4e4;
    --white: #ffffff;
    --grey-text: #6b6b6b;
  }
  html, body {
    margin: 0;
    width: 1200px;
    height: 900px;
    overflow: hidden;
    background: var(--backdrop);
  }
  .canvas {
    position: relative;
    width: 1200px;
    height: 900px;
  }
  .card {
    position: absolute;
    overflow: hidden;
    box-shadow: 0 10px 30px rgba(0,0,0,0.35);
  }
  .card svg { position: absolute; inset: 0; display: block; }

  /* Front */
  .card-front { left: 60px; top: 280px; width: 620px; height: 360px; }
  .company-name {
    position: absolute; left: 222px; top: 62px;
    font-family: "Crimson Text", serif; font-size: 26px; color: var(--navy);
    letter-spacing: 0.3px; white-space: nowrap;
  }
  .person { position: absolute; left: 42px; top: 176px; font-family: "Open Sans", sans-serif; }
  .person-name { font-size: 26px; font-weight: 600; color: var(--navy); margin: 0; white-space: nowrap; }
  .person-role { font-size: 11px; color: var(--grey-text); margin: 2px 0 0 2px; }
  .brand-mark {
    position: absolute; right: 70px; bottom: 64px;
    display: flex; align-items: center; gap: 10px; white-space: nowrap;
    font-family: "Open Sans", sans-serif; font-size: 13px; font-weight: 600; color: var(--navy);
  }
  .brand-dot { width: 46px; height: 46px; border-radius: 50%; background: var(--gold); flex: none; }

  /* Back */
  .card-back { left: 800px; top: 160px; width: 330px; height: 578px; }
  .back-text {
    position: absolute; left: 34px;
    font-family: "Open Sans", sans-serif; font-size: 12px; line-height: 1.55; color: var(--white);
    white-space: nowrap;
  }
  .address { top: 40px; }
  .contacts { top: 300px; }
  .back-text p { margin: 0; }
</style>
</head>
<body>
<main class="canvas">

  <section class="card card-front" aria-label="Card front">
    <svg width="620" height="360" viewBox="0 0 620 360" aria-hidden="true">
      <rect width="620" height="360" fill="var(--gold)"/>
      <ellipse cx="200" cy="180" rx="456" ry="210" fill="var(--navy)"/>
      <ellipse cx="196" cy="180" rx="440" ry="198" fill="var(--paper)"/>
    </svg>
    <div class="company-name">Lumen Bridge Partners Limited</div>
    <div class="person">
      <p class="person-name">Dana Whitfield</p>
      <p class="person-role">PR Consultant</p>
    </div>
    <div class="brand-mark">
      <span class="brand-dot"></span>
      <span>Lumen Bridge Partners Limited</span>
    </div>
  </section>

  <section class="card card-back" aria-label="Card back">
    <svg width="330" height="578" viewBox="0 0 330 578" aria-hidden="true">
      <rect width="330" height="578" fill="var(--gold)"/>
      <path d="M0 260 H330 V450 Q200 540 0 470 Z" fill="var(--white)"/>
      <path d="M0 260 H330 V430 Q200 520 0 452 Z" fill="var(--navy)"/>
    </svg>
    <div class="back-text address">
      <p>Headquarters (Hong Kong)</p>
      <p>Unit 8, 14/F Harbour Crest Tower,</p>
      <p>27 Lantern Road Central,</p>
      <p>Hong Kong</p>
      <p>www.lumen-bridge-partners.example</p>
    </div>
    <div class="back-text contacts">
      <p>E-mail : dana@lumen-bridge-partners.example</p>
      <p>Mobile : (852) 5550 0142</p>
      <p>Tel : (852) 5550 0187</p>
      <p>Fax : (852) 5550 0193</p>
    </div>
  </section>

</main>
</body>
</html>
```